Brisk Lantern Estates, which offers a selection of prime properties (villas

A website that contains: Idea, benefits, destinations (villas), offers, about us, contact, newsletter, social media, blog, look at the attachment, even if it is in German. The idea is that I can easily add new pages, if necessary, with the design you make. Later on we want to add a reservation system, so you can book your villa through the internet. Besides, there is a concierge service available, which organizes everything for the customer, owner, from villa to restaurant, limo service, ... & benefits and emotions through nice pictures / videos, they should be convinced to invest.

Target Market(s)

Investors (golfer and non-golfer) which have 300'000 to invest in a kind of real-estate investing club

Number of Pages Required

5+ page

Font styles to use
Sans Serif

Requirements
Must have
• It must be for wordpress, must have an exclusive touch, high quality, with nice pictures of golf courses. The Logo is gold so it has to match with gold, the font is segan or segoe semilight or similar, sans serif
Nice to have
• may be as well as the possibility to include videos of the different destinations and houses

```html
<!DOCTYPE html>
<html lang="en">
<head>
<meta charset="utf-8">
<title>Brisk Lantern Estates</title>
<link href="https://fonts.googleapis.com/css2?family=Oswald:wght@300;400&family=Open+Sans:wght@300;400;600;700&display=swap" rel="stylesheet">
<style>
:root{
  --gold:#d4a52c;
  --gold-dark:#a8821f;
  --ink:#161616;
  --panel:#1f1f1f;
  --panel-2:#2a2a2a;
  --row:#2c2c2c;
  --text:#9a9a9a;
  --text-light:#c9c9c9;
  --stage:#dfe6ea;
}
*{margin:0;padding:0;box-sizing:border-box}
html,body{width:1200px;height:1200px;overflow:hidden;background:var(--stage)}
body{position:relative;font-family:"Open Sans",sans-serif;color:var(--text)}
.page{position:absolute;left:485px;top:24px;width:232px;height:1154px;overflow:hidden;background:var(--ink)}
section,header,footer{position:relative;overflow:hidden}
.h-title{font-family:"Oswald",sans-serif;font-weight:300;color:var(--gold);text-align:center;font-size:6px;letter-spacing:.1px}
.h-title::before{content:"";display:block;width:18px;height:.5px;background:#555;margin:0 auto 2px}
.h-title::after{content:"";display:block;width:18px;height:.5px;background:#555;margin:2px auto 0}
.kicker{font-family:"Oswald",sans-serif;color:#ddd;font-size:2.2px;text-align:center;letter-spacing:.2px}
p,li{font-size:2.3px;line-height:3.2px}
ul{list-style:none}
li::before{content:"";display:inline-block;width:1.2px;height:1.2px;border-radius:50%;background:#ccc;margin-right:1px;vertical-align:middle}

/* nav */
.nav{height:21px;background:#111;display:flex;align-items:center;padding:0 4px 0 26px}
.brand{display:flex;flex-direction:column;align-items:center;gap:1px}
.brand-mark{width:7px;height:5px;border:.6px solid var(--gold)}
.brand-name{font-family:"Oswald",sans-serif;font-weight:300;font-size:2.6px;color:var(--gold);white-space:nowrap}
.menu{display:flex;gap:6px;margin-left:8px;font-size:2px;color:#bbb;text-transform:uppercase}
.menu .on{color:var(--gold)}
.nav-btn{margin-left:6px;background:var(--gold);color:#111;font-size:1.8px;padding:1.2px 3px;font-weight:700}
.socials{display:flex;gap:1px;margin-left:3px}
.socials span{width:5px;height:5px;background:#4c6db1}
.socials span:last-child{background:#c8372c}

/* hero */
.hero{height:99px}
.hero-photo{position:absolute;inset:0;background:linear-gradient(180deg,#6b8db3 0%,#b9d0e0 35%,#4e6e54 60%,#2d3b22 100%)}
.hero-caption{position:absolute;left:-8px;top:47px;width:58px;height:48px;background:rgba(20,20,20,.8);padding:5px 0 0 0;font-family:"Oswald",sans-serif;color:#fff;white-space:nowrap}
.hero-caption .small{font-size:2.2px;padding-left:8px}
.hero-caption .big{font-size:9px;color:var(--gold);line-height:9px}
.hero-caption .mid{font-size:4.5px;color:var(--gold);line-height:5px}
.hero-caption .tag{font-size:3.4px;line-height:4px}
.hero-caption .price{font-size:6.5px;line-height:8px}
.enquiry{position:absolute;right:26px;top:8px;width:64px;height:88px;background:rgba(15,15,15,.82);padding:3px 4px}
.enquiry h3{font-size:3px;color:#fff;text-align:center;font-weight:600;margin-bottom:1.5px}
.enquiry .note{font-size:1.8px;text-align:center;color:#ccc;margin-bottom:2px}
.field{height:5px;border:.4px solid #666;background:rgba(255,255,255,.08);font-size:1.6px;color:#aaa;padding:1.4px 2px;margin-bottom:2.2px}
.field.row{display:flex;gap:2px;border:none;background:none;padding:0}
.field.row span{border:.4px solid #666;background:rgba(255,255,255,.08);padding:1.4px 2px}
.field.row span:last-child{flex:1}
.enquire-btn{margin-top:3px;height:6px;background:var(--gold);color:#fff;font-size:2px;font-weight:700;text-align:center;line-height:6px}

/* idea */
.idea{height:110px;padding-top:14px;border-bottom:2px solid #2a2a2a}
.idea-body{display:flex;margin-top:6px;padding-left:25px;gap:8px}
.founders{display:flex;margin-top:14px}
.portrait{width:35px;height:35px;border-radius:50%;border:1px solid #ddd;background:radial-gradient(circle at 50% 40%,#8a8f96,#3b3f44)}
.portrait+.portrait{margin-left:-6px}
.idea-text{width:110px}
.idea-text p{margin-bottom:3px}
.idea-text .lead{color:var(--gold);font-weight:700;margin-top:6px;border-top:.4px solid #333;padding-top:3px}
.cols{display:grid;grid-template-columns:1fr 1fr}

/* offer */
.offer{height:128px;background:var(--panel-2);padding-top:9px}
.offer svg{position:absolute;left:0;top:28px}
.offer-note{position:absolute;font-size:2.2px;line-height:3px;text-align:center;width:50px}

/* map */
.map-row{height:91px;display:flex;border-bottom:.5px solid #333}
.map{width:74px;height:100%;background:linear-gradient(135deg,#f1eee6,#dfe4ea)}
.map-text{flex:1;padding:9px 8px 0 8px}
.map-text .h-title{margin-bottom:5px}
.map-text p{margin-bottom:2px}
.map-text .lead{color:var(--gold);font-weight:700;margin-top:4px}
.map-text ul{display:grid;grid-template-columns:1fr 1fr 1fr;font-size:1.8px}
.map-text li{font-size:1.8px;line-height:2.8px}

/* gallery */
.gallery{height:87px;background:var(--gold);padding-top:9px}
.gallery .h-title{color:#222}
.gallery .h-title::before,.gallery .h-title::after{background:#8a6b19}
.cards{display:flex;gap:4px;position:absolute;left:-32px;top:27px}
.card{width:55px;height:56px;background:#fff;padding:1px}
.card .ph{height:46px;background:linear-gradient(180deg,#88a9c9,#b68257 60%,#4a7fa8)}
.card:nth-child(3) .ph{background:linear-gradient(180deg,#9cb7d0,#6f9a55 60%,#3b6e3c)}
.card:nth-child(4) .ph{background:linear-gradient(180deg,#c8d6e2,#8ea36b 55%,#5b6f4a)}
.card:nth-child(5) .ph{background:linear-gradient(180deg,#a6bfd6,#7b8e5a 60%,#cdb79a)}
.card .cap{display:flex;justify-content:space-between;align-items:center;font-family:"Oswald",sans-serif;font-size:2px;color:#333;padding:2px 1px 0}
.card .cap i{width:3px;height:3px;border-radius:50%;border:.4px solid #333}

/* benefits */
.benefit{padding-top:12px}
.benefit .h-title{font-size:6.5px;margin-bottom:8px}
.benefit .h-title::before{display:none}
.benefit .h-title::after{display:none}
.benefit-body{display:flex;gap:10px;padding:0 25px}
.benefit-photo{width:71px;flex:none;border:.6px solid #ddd}
.benefit-text p{margin-bottom:2px}
.b1{height:104px}
.b1 .benefit-photo{height:68px;background:linear-gradient(180deg,#c7d4de,#c9a57e 45%,#5f8a45 65%,#5a6a6a)}
.b2{height:98px}
.b2 .benefit-photo{height:68px;background:linear-gradient(180deg,#4a4a4a,#b4753f 50%,#3f79b7)}
.b3{height:88px}
.b3 .benefit-photo{height:61px;background:linear-gradient(180deg,#8fa3b7,#6f8a5a 55%,#5b4a3a)}

.club{height:93px;padding-top:8px;background:linear-gradient(180deg,#2f2d28,#25241f 60%,#1e1e1c)}
.club .h-title{margin-bottom:5px}
.club p{text-align:center;padding:0 44px;margin-bottom:.8px;font-size:2.1px;line-height:3px}

/* investment table */
.plans{height:181px;padding-top:12px;background:#1a1a1a}
.plans .h-title{font-size:6px;margin-bottom:12px}
.plans .h-title::after{display:none}
.plan-grid{display:grid;grid-template-columns:repeat(3,1fr);gap:2px;margin:0 26px}
.plan{display:flex;flex-direction:column;gap:3px}
.cell{background:var(--row);padding:2px 2px;min-height:9px}
.cell.head{background:#2e2e2e}
.cell .name{font-family:"Oswald",sans-serif;color:var(--gold);font-size:2.4px}
.cell .price{font-size:2.1px;color:#ccc;margin-top:1px}
.cell .lbl{font-size:1.8px;font-weight:700;color:#ddd}
.cell p{font-size:1.7px;line-height:2.4px}
.cell.tall{min-height:19px}

/* footer */
.footer{height:42px;background:#101010;display:flex;padding:5px 26px 0;gap:8px}
.pin{width:6px}
.footer p{font-size:1.7px;line-height:2.5px}
.foot-brand{margin-left:auto;display:flex;flex-direction:column;align-items:center;margin-top:2px;margin-right:8px}
.foot-brand .brand-mark{width:14px;height:10px}
.foot-brand .brand-name{font-size:4px;margin-top:1px}
.foot-brand p{font-size:1.4px;text-align:center}
.copy{height:8px;background:#2b2b2b;font-size:1.6px;text-align:center;line-height:8px;color:#777}
</style>
</head>
<body>
<main class="page">

  <header class="nav">
    <div class="brand"><span class="brand-mark"></span><span class="brand-name">BRISK LANTERN ESTATES</span></div>
    <nav class="menu"><span class="on">Home</span><span>About us</span><span>Destinations</span><span>Benefits</span><span>Contact</span></nav>
    <span class="nav-btn">ENQUIRE NOW</span>
    <div class="socials"><span></span><span></span><span></span></div>
  </header>

  <section class="hero">
    <div class="hero-photo" role="img" aria-label="Villa terrace pavilion overlooking the sea and palm garden"></div>
    <div class="hero-caption">
      <div class="small">INVESTING IN</div>
      <div class="big">REAL ESTATE</div>
      <div class="mid">INVESTMENT</div>
      <div class="tag">LIFESTYLE TOGETHER</div>
      <div class="small">STARTING FROM</div>
      <div class="price">CHF 18,000</div>
    </div>
    <form class="enquiry">
      <h3>Register Your Interest</h3>
      <div class="note">We welcome every enquiry</div>
      <div class="field">Select Title</div>
      <div class="field">First Name</div>
      <div class="field">Last Name</div>
      <div class="field">Email Address</div>
      <div class="field row"><span>Swiss</span><span>+41 Phone Number</span></div>
      <div class="enquire-btn">ENQUIRE NOW</div>
    </form>
  </section>

  <section class="idea">
    <h2 class="h-title">OUR IDEA</h2>
    <div class="idea-body">
      <div class="founders">
        <div class="portrait" role="img" aria-label="Portrait of founder"></div>
        <div class="portrait" role="img" aria-label="Portrait of co-founder"></div>
      </div>
      <div class="idea-text">
        <ul>
          <li>The idea follows a need for holidays, variety and enjoyment at the highest level &amp; at attractive conditions.</li>
        </ul>
        <p></p>
        <ul>
          <li>The concept is based on many discussions and has been developed with the help of various experts from various fields.</li>
        </ul>
        <p class="lead">Real estate in golf resorts are appreciated by golfers as non-golfers. The reasons are:</p>
        <ul class="cols">
          <li>Quiet</li><li>Well maintained park landscape</li>
          <li>Resort infrastructure &amp; Services</li><li>Worth preserving</li>
        </ul>
      </div>
    </div>
  </section>

  <section class="offer">
    <h2 class="h-title">OUR OFFER</h2>
    <svg width="232" height="100" viewBox="0 0 232 100" aria-hidden="true">
      <g fill="none" stroke="#555" stroke-width=".4">
        <line x1="46" y1="16" x2="72" y2="16"/><line x1="64" y1="56" x2="96" y2="56"/>
        <line x1="81" y1="97" x2="112" y2="97"/><line x1="166" y1="38" x2="136" y2="38"/>
        <line x1="159" y1="78" x2="124" y2="78"/>
      </g>
      <g fill="var(--gold)">
        <circle cx="46" cy="16" r="1.3"/><circle cx="64" cy="56" r="1.3"/><circle cx="81" cy="97" r="1.3"/>
        <circle cx="176" cy="38" r="1.3"/><circle cx="159" cy="78" r="1.3"/>
      </g>
      <polygon points="72,6 164,6 118,100" fill="var(--gold)"/>
      <g stroke="#2a2a2a" stroke-width="1">
        <line x1="80" y1="24" x2="156" y2="24"/><line x1="89" y1="42" x2="147" y2="42"/>
        <line x1="98" y1="61" x2="138" y2="61"/><line x1="107" y1="79" x2="129" y2="79"/>
      </g>
      <g fill="none" stroke="#fff" stroke-width=".6">
        <rect x="113" y="10" width="10" height="8"/><polyline points="114,16 117,13 119,15 122,11"/>
        <circle cx="118" cy="33" r="4.5"/><line x1="113.5" y1="33" x2="122.5" y2="33"/><ellipse cx="118" cy="33" rx="2" ry="4.5"/>
        <path d="M112 56h12v-3h-3v-2h-2v2h-3v-2h-2v2h-2z"/>
        <rect x="113" y="67" width="10" height="6" rx="1"/><circle cx="118" cy="70" r="1.5"/>
        <rect x="114" y="84" width="8" height="5"/>
      </g>
    </svg>
    <p class="offer-note" style="left:24px;top:46px">We offer private individuals and companies fund shares in Brisk Lantern Estates.</p>
    <p class="offer-note" style="left:36px;top:88px">You can enjoy some memorable vacation weeks, play golf and use the resort services with family and friends.</p>
    <p class="offer-note" style="left:58px;top:131px">You benefit from an increase in the value of the portfolio.</p>
    <p class="offer-note" style="left:150px;top:76px">With these you become co-owner of a worldwide diversified portfolio of exclusive and stylish villas / apartments in World Class golf resorts.</p>
    <p class="offer-note" style="left:128px;top:116px">We rent the remaining weeks in the best possible way on the market, at maximum achievable prices, which in turn benefits you.</p>
  </section>

  <section class="map-row">
    <div class="map" role="img" aria-label="Map of Spain and Portugal with resort locations marked"></div>
    <div class="map-text">
      <h2 class="h-title">REAL ESTATE PORTFOLIO</h2>
      <p>5 properties in Spain and Portugal, for a purchase price of around CHF 9 million (including furniture and golf membership), are intended for take-off.</p>
      <p>Und zw ca. 50% über das Fondsvermögen und 50% über Hypotheken lokaler Banken zu finanzieren.</p>
      <p class="lead">Die Immobilienauswahl und der Kauf erfolgt durch ein Expertengremium aus den Bereichen:</p>
      <ul><li>Recht</li><li>Immobilien</li><li>Versicherungen</li><li>Wirtschaftsprüfung</li><li>Golf</li></ul>
    </div>
  </section>

  <section class="gallery">
    <h2 class="h-title">REAL ESTATE PORTFOLIO</h2>
    <div class="cards">
      <div class="card"><div class="ph" role="img" aria-label="Modern villa with pool"></div><div class="cap"><span>LOREM IPSUM</span><i></i></div></div>
      <div class="card"><div class="ph" role="img" aria-label="Lit villa with pool at dusk"></div><div class="cap"><span>MOREM IPSUM SUN</span><i></i></div></div>
      <div class="card"><div class="ph" role="img" aria-label="Golf course green with fountain"></div><div class="cap"><span>LOREM IPSUM SEA</span><i></i></div></div>
      <div class="card"><div class="ph" role="img" aria-label="Resort houses beside a lake"></div><div class="cap"><span>MOREM PIPS LORTE</span><i></i></div></div>
      <div class="card"><div class="ph" role="img" aria-label="Terrace with mountain view"></div><div class="cap"><span>REAL ESTATE IPSUM</span><i></i></div></div>
    </div>
  </section>

  <section class="benefit b1">
    <div class="kicker">YOUR BENEFIT</div>
    <h2 class="h-title">MONETARY</h2>
    <div class="benefit-body">
      <div class="benefit-photo" role="img" aria-label="Villas beside a golf course lake"></div>
      <div class="benefit-text">
        <p>Sie sind Miteigentümer von exklusiven Immobilien in Topresorts, in wunderschönen, gepflegten und sicherer Umgebung.</p>
        <p>Anlageformen ermöglicht Reisen, Ihre Ferien an verschiedenen Destinationen zu verbringen – Abwechslung ist garantiert.</p>
        <p>Sie geniessen:</p>
        <ul>
          <li>Die Privatsphäre in Ihrer Feriendes, weitweit mit Familie und Freunden</li>
          <li>Ihr Spiel auf Top Golfplätzen und den Zugang zu privaten Anlagen</li>
          <li>Den Besuch der Sehenswürdigkeiten</li>
          <li>Kulinarische Highlights in besten Restaurants</li>
          <li>Kulturelle Highlights in der jeweiligen Stadt</li>
        </ul>
        <p>Sie fördern die nachhaltige Nutzung von Immobilien.</p>
        <p>Sie erhalten einen unbezahlbaren Erlebnismehrwert.</p>
      </div>
    </div>
  </section>

  <section class="benefit b2">
    <div class="kicker">IHR NUTZEN</div>
    <h2 class="h-title">PRAKTISCH</h2>
    <div class="benefit-body">
      <div class="benefit-text">
        <p>Sie besitzen Immobilien, ohne sich um den Kauf, Verwaltung und den Unterhalt kümmern zu müssen.</p>
        <p>Das Verhältnis von 4 Investoren auf 1 Immobilie garantiert eine sehr gute Verfügbarkeit.</p>
        <p>Im Gegensatz zu Reiseformen, kann das ganze Jahr über Golf gespielt und womit die Immobilien genutzt werden.</p>
        <p>Sie bestimmen die Investmentdrittel und der Anzahl Ferienwochen, welche Sie in Ihren Immobilien verbringen wollen.</p>
        <p>Sie wohnen immer privat, mit viel Platz und können anderenseits von den Hotelservices, Sport-, Wellness- &amp; Gastronomieangeboten des Resorts profitieren.</p>
        <p>Ihnen steht einen Concierge Service zur Verfügung, welcher für Sie alles organisiert. Sie vor Ort betreut und mit Geheimtipps versorgt.</p>
      </div>
      <div class="benefit-photo" role="img" aria-label="Modern villa with illuminated pool at dusk"></div>
    </div>
  </section>

  <section class="benefit b3">
    <div class="kicker">IHR NUTZEN</div>
    <h2 class="h-title">MONETAR</h2>
    <div class="benefit-body">
      <div class="benefit-photo" role="img" aria-label="Terrace lounge overlooking golf course and mountains"></div>
      <div class="benefit-text">
        <p>Sie werden mit einer verhältnismässig geringen Investition Miteigentümer mehrerer exklusiver Immobilien.</p>
        <p>Sie teilen die Kauf- und Verwaltungsgebühren mit anderen Eigentümern.</p>
        <p>Sie sparen bei Ihren Ferien mindestens 1/3 des marktüblichen Mietpreises für gleichwertige Ferienimmobilien.</p>
        <p>Sie profitieren von einer Wertsteigerung des Portfolios.</p>
        <p>Sie profitieren über den Fonds von den Mieteinnahmen der Immobilien im Portfolio.</p>
      </div>
    </div>
  </section>

  <section class="club" role="img" aria-label="Dimmed resort clubhouse background">
    <h2 class="h-title">MONETAR</h2>
    <p>Als Investor werden Sie Mitglied im Brisk Lantern Owners Club, welcher mittels des Concierge Services die Nutzung regelt und organisiert.</p>
    <p>Auf eine Immobilie kommen nur 4 Investoren – damit ist eine gute Verfügbarkeit gewährleistet.</p>
    <p>Mit einer geplanten Nutzung von je 8 Wochen, wird eine Belegung von 16 Wochen erzielt. Somit bleiben max. 36 Wochen für Zusatzwochen der Mitglieder und die Vermietung im freien Markt.</p>
    <p>Jede Immobilie hat einen Immobilienfachmann und einen Mietverwalter, welche multiplizierte Instandhaltung sichern. Die Golfhallen haben einen Wert von CHF 110.</p>
    <p>Gemäss Investment, erhält der Investor jedes Jahr ein Golfhallguthaben für die Nutzung der Immobilien.</p>
    <p>Er kann jedoch sein Guthaben auch ins nächste Jahr nehmen, wenn es wurden übertragen oder dem Club-Management anbieten.</p>
    <p>Der Mitgliederrat hat je CHF verfügbar auch Zusatzwochen kaufen.</p>
  </section>

  <section class="plans">
    <h2 class="h-title">INVESTMENTOPTIONEN FÜR PRIVATPERSONEN UND FIRMEN</h2>
    <div class="plan-grid">
      <div class="plan">
        <div class="cell head"><div class="name">OWNERSHIP ALBATROS:</div><div class="price">CHF 350'000.-</div></div>
        <div class="cell tall"><div class="lbl">GUTHABEN:</div><p>380 Golfbälle, entspricht ca. 7 Wochen Ferien, jederzeit einlösbar</p></div>
        <div class="cell tall"><div class="lbl">JAHRESGEBÜHR:</div><div class="price">CHF 16'000.-</div></div>
        <div class="cell tall"><div class="lbl">NUTZEN:</div><p>Nutzung, jegliche Kosten der Immobilien, Concierge Service, Golf-Fees im Resort, Wertsteigerung</p></div>
        <div class="cell tall"><div class="lbl">AUSSTIEG:</div><p>Nutzung, jegliche Kosten der Immobilien, Concierge Service, Golf-Fees im Resort, Wertsteigerung</p></div>
      </div>
      <div class="plan">
        <div class="cell head"><div class="name">OWNERSHIP EAGLE:</div><div class="price">CHF 250'000.-</div></div>
        <div class="cell tall"><div class="lbl">GUTHABEN:</div><p>180 Golfbälle, entspricht ca. 5 Wochen Ferien, nach Wunsch einlösbar Ferien im Portfolio</p></div>
        <div class="cell tall"><div class="lbl">JAHRESGEBÜHR:</div><div class="price">CHF 16'000.-</div></div>
        <div class="cell tall"><div class="lbl">NUTZEN:</div><p>Nutzung, jegliche Kosten der Immobilien, Concierge Service, Golf-Fees im Resort, Wertsteigerung</p></div>
        <div class="cell tall"><div class="lbl">AUSSTIEG:</div><p>nach 7 Jahren jederzeit, falls ein Käufer für die Anteile vorhanden ist, sonst an den Fonds</p></div>
      </div>
      <div class="plan">
        <div class="cell head"><div class="name">OWNERSHIP BIRDIE:</div><div class="price">CHF 300'000.-</div></div>
        <div class="cell tall"><div class="lbl">GUTHABEN:</div><p>Kein</p></div>
        <div class="cell tall"><div class="lbl">JAHRESGEBÜHR:</div><div class="price">KEINE</div></div>
        <div class="cell tall"><div class="lbl">NUTZEN:</div><p>Wertsteigerung Portfolio</p></div>
        <div class="cell tall"><div class="lbl">AUSSTIEG:</div><p>nach 7 Jahren jederzeit, falls ein Käufer für die Anteile vorhanden ist, sonst an den Fonds</p></div>
      </div>
    </div>
  </section>

  <footer class="footer">
    <svg class="pin" width="6" height="8" viewBox="0 0 6 8" aria-hidden="true"><path d="M3 0a3 3 0 0 1 3 3c0 2-3 5-3 5S0 5 0 3a3 3 0 0 1 3-3z" fill="var(--gold)"/><circle cx="3" cy="3" r="1" fill="#101010"/></svg>
    <div>
      <p>Address details</p>
      <p>Brisk Lantern Estates</p>
      <p>c/o Harbour Lane Trust GmbH, Aldenweg 14</p>
      <p>CH-8000 Tannen am See</p>
      <p>Suisse / Switzerland</p>
      <p>Tel. +41 00 000 00 00 · Fax +41 00 000 00 01</p>
      <p>Mail: info@brisklantern.ch</p>
    </div>
    <div style="width:44px">
      <p>About us</p>
      <p>Investor-focused ownership in premium golf resort homes with full concierge care and transparent shared costs.</p>
    </div>
    <div class="foot-brand">
      <span class="brand-mark"></span>
      <span class="brand-name">BRISK LANTERN ESTATES</span>
      <p>a member of investing golf communities</p>
    </div>
  </footer>
  <div class="copy">Copyright 2016 · Brisk Lantern Estates</div>

</main>
</body>
</html>
```